Brindlewood Chamber Home Page - Make it more modern a little bit futuristic

Take existing site and make it more modern and a little bit futuristic.
Design of new homepage with slightly more futuristic feel.

I don't the current design. There has recently been a change of direction of the chamber partly driven by COVID to move more meetings online instead of face to face. We want to inspire our members to embrace technology. We also want to position our city as a great modern place to business. We want to do that by featuring our great members on the home page. We also want to promote events on the home page. We also want to convert new visitors to members.

Members should be able to login to manage their membership. Visitors should be able to search for members by category, member name, member company.

It should look premium corporate but more futuristic and forward looking than the neighbouring Chambers:
https://www.velmarchcrestchamber.com.au/
https://www.tanwickharbourchamber.org.au/
https://orlundchamber.org.au/
https://quillmereshorechamber.org.au/#!event-list
https://directory.businessdalvenshireregion.com.au/businesses/n-t/ashgrove-falls-chamber-of-commerce

Target Market(s)

Modern small businesses owners

Industry/Entity Type

Business

Number of Pages Required

1 page

Font styles to use
Sans Serif

Requirements
Must have
• Appeal to small business owners
Responsive down to mobile
Nice to have
• Draw a focus to members from directory
Either a white background or black background
I really like the Tarrowby Heights Chamber home page at: https://thchamber-example.com/
Should not have
• Must look more modern than their existing site at: https://www.velmarchcrestchamber.com.au/
No significant changes to logo
Don't like the light blue on existing site.

```html
<!DOCTYPE html>
<html lang="en">
<head>
<meta charset="utf-8">
<title>Brindlewood Chamber of Commerce</title>
<link href="https://fonts.googleapis.com/css2?family=Poppins:wght@400;500;600&family=Tinos&display=swap" rel="stylesheet">
<style>
:root{
  --navy:#132a52;
  --navy-deep:#0d1a33;
  --ink:#2b2b2b;
  --gold:#f3b11c;
  --orange:#f5a11b;
  --white:#ffffff;
  --muted:#6b6b6b;
  --social:#4b5fa8;
}
*{margin:0;padding:0;box-sizing:border-box}
html,body{width:1200px;height:3845px;overflow:hidden;background:var(--white)}
body{font-family:'Poppins',sans-serif;color:var(--ink);position:relative}
.abs{position:absolute}
a{color:inherit;text-decoration:none}

/* Hero */
.hero-photo{left:0;top:0;width:1200px;height:745px;background:radial-gradient(ellipse at 70% 55%,#3c4c78 0%,#1b2748 45%,#0d1428 100%)}
.hero-cut{left:0;top:600px;width:1200px;height:160px}
.logo{left:100px;top:45px;display:flex;align-items:center;gap:14px;color:var(--white)}
.logo-mark{width:70px;height:70px;background:var(--gold)}
.logo-name{font-size:34px;font-weight:500;letter-spacing:2px;line-height:1}
.logo-sub{font-size:12px;letter-spacing:1.5px;margin-top:4px}
.topbar{top:22px;left:590px;display:flex;align-items:center;color:var(--white);font-size:15px}
.social-dot{width:14px;height:14px;border:1.5px solid #cfd5e3;border-radius:50%;margin-right:26px}
.topbar .link{margin-left:18px;margin-right:42px}
.topbar .link:first-of-type{margin-left:0}
.phone{display:flex;align-items:center;gap:8px}
.nav{top:76px;left:490px;width:610px;display:flex;justify-content:space-between;padding:0 13px;color:var(--white);font-size:16px;border-bottom:1px solid rgba(255,255,255,.45);height:37px}
.nav .active{color:var(--orange);position:relative}
.nav .active::after{content:"";position:absolute;left:50%;bottom:-9px;width:12px;height:3px;margin-left:-6px;background:var(--orange)}
.hero-title{top:236px;left:0;width:1200px;text-align:center;color:var(--white);font-family:'Tinos',serif;font-size:38px;line-height:51px;letter-spacing:1px}
.search{left:193px;top:351px;width:815px;height:97px;background:rgba(0,0,0,.85);padding:13px 20px}
.field{position:absolute;top:13px}
.field label{display:block;color:var(--white);font-size:14px;margin-bottom:7px}
.select{height:42px;background:#fff;border:1px solid #ddd;display:flex;align-items:center;justify-content:space-between;padding:0 18px;font-size:14px;color:#666}
.btn-explore{left:509px;top:479px;width:182px;height:51px;background:var(--navy);color:var(--white);font-size:19px;display:flex;align-items:center;justify-content:center;gap:14px}

/* Welcome */
.welcome-title{left:121px;top:832px;font-size:35px;font-weight:500;line-height:44px;color:#222}
.body-copy{font-size:14px;line-height:24px;color:#333}
.welcome-copy{left:121px;top:946px;width:590px}
.body-copy p{margin-bottom:6px}
.btn-navy{background:var(--navy);color:var(--white);font-size:15px;display:flex;align-items:center;justify-content:center;gap:8px}
.btn-learn{left:119px;top:1110px;width:149px;height:44px}
.welcome-photo{left:772px;top:833px;width:279px;height:279px;background:linear-gradient(135deg,#5a6b80,#c9d3dc 55%,#38495e)}

/* Services band */
.services-bg{left:0;top:1210px;width:1200px;height:720px}
.card{width:235px;text-align:center;padding:30px 18px 0}
.card h3{font-size:16px;font-weight:500;margin:12px 0 10px}
.card p{font-size:12px;line-height:18px}
.card-light{background:var(--white);color:#222;height:229px}
.card-dark{border:2px solid #e8ecf4;color:var(--white);background:rgba(13,26,51,.35)}
.card-light p{color:#444}

/* Book */
.book-title{left:128px;top:2026px;font-size:32px;font-weight:500;line-height:40px;color:#222}
.book-copy{left:128px;top:2140px;width:540px}
.book-copy u{color:var(--navy)}
.book-art{left:736px;top:1970px;width:309px;height:436px;background:linear-gradient(160deg,#f0b22a 0%,#f5c457 45%,#f7f7f7 46%,#e2e2e2 100%)}

/* Connect band */
.connect-bg{left:0;top:2420px;width:1200px;height:620px}
.connect-title{left:0;top:2632px;width:1200px;text-align:center;color:var(--white);font-size:29px;font-weight:500}
.connect-sub{left:0;top:2680px;width:1200px;text-align:center;color:var(--white);font-size:19px}
.btn-connect{left:431px;top:2772px;width:360px;height:62px;background:var(--social);color:var(--white);font-size:20px;font-weight:500;display:flex;align-items:center;justify-content:center;gap:16px;letter-spacing:.5px}
.btn-connect span.sq{width:26px;height:26px;background:var(--white);border-radius:3px}

/* Sponsors */
.sponsor-title{left:0;top:3094px;width:1200px;text-align:center;font-size:29px;font-weight:500;line-height:42px;color:#222}
.sponsors{left:161px;top:3209px;width:879px;height:112px;display:flex}
.sponsor{flex:1;display:flex;align-items:center;justify-content:center;border-left:1px solid #e5e5e5;border-right:1px solid #e5e5e5;margin:0 5px;font-size:20px;font-weight:500;color:#7d7d7d}

/* Footer */
.footer-bg{left:0;top:3400px;width:1200px;height:445px}
.fcol{top:3556px;color:var(--white);font-size:12px}
.fcol h4{font-size:12px;font-weight:600;margin-bottom:18px;letter-spacing:.4px}
.fcol li{list-style:none;line-height:24px}
.contact-row{display:flex;gap:10px;margin-bottom:14px;line-height:18px}
.contact-row svg{flex:none;margin-top:2px}
.subscribe{margin-top:16px;display:flex;width:256px;height:35px;border-radius:18px;overflow:hidden}
.subscribe .input{flex:1;background:var(--white);color:#888;display:flex;align-items:center;padding-left:22px}
.subscribe .go{width:108px;background:var(--gold);display:flex;align-items:center;justify-content:center;font-weight:500}
.footer-line{left:0;top:3776px;width:1200px;height:1px;background:rgba(255,255,255,.15)}
.copyright{left:107px;top:3797px;color:var(--white);font-size:12px}
.foot-social{left:962px;top:3798px;display:flex;gap:16px}
.foot-social span{width:13px;height:13px;border:1.5px solid #8d97ad;border-radius:50%}
</style>
</head>
<body>

<!-- Hero -->
<div class="abs hero-photo" role="img" aria-label="Hand touching a glowing tablet with floating app icons"></div>
<svg class="abs hero-cut" viewBox="0 0 1200 160" preserveAspectRatio="none">
  <polygon points="0,118 1200,0 1200,20 0,140" fill="#132a52"/>
  <polygon points="0,128 1200,10 1200,14 0,134" fill="#f3b11c"/>
  <polygon points="0,140 1200,20 1200,160 0,160" fill="#ffffff"/>
</svg>

<div class="abs logo">
  <div class="logo-mark"></div>
  <div><div class="logo-name">BRINDLEWOOD</div><div class="logo-sub">CHAMBER OF COMMERCE</div></div>
</div>

<div class="abs topbar">
  <span class="social-dot"></span><span class="social-dot"></span><span class="social-dot"></span><span class="social-dot" style="margin-right:40px"></span>
  <a class="link" href="#">Join</a><a class="link" href="#">Login</a>
  <span class="phone"><svg width="16" height="16" viewBox="0 0 24 24"><path d="M6.6 10.8a15 15 0 006.6 6.6l2.2-2.2a1 1 0 011-.25 11.4 11.4 0 003.6.57 1 1 0 011 1V20a1 1 0 01-1 1A17 17 0 013 4a1 1 0 011-1h3.5a1 1 0 011 1c0 1.25.2 2.45.57 3.57a1 1 0 01-.25 1z" fill="#fff"/></svg>+61 7 5550 1842</span>
</div>

<nav class="abs nav">
  <a class="active" href="#">Home</a><a href="#">Membership</a><a href="#">Events</a><a href="#">Benefits</a><a href="#">About Us</a><a href="#">Contact</a>
</nav>

<h1 class="abs hero-title">WELCOME TO BRINDLEWOOD<br>CHAMBER OF COMMERCE</h1>

<div class="abs search">
  <div class="field" style="left:20px;width:287px"><label>Members Category</label><div class="select">Category Select <svg width="14" height="8" viewBox="0 0 14 8"><path d="M1 1l6 6 6-6" stroke="#555" fill="none" stroke-width="1.5"/></svg></div></div>
  <div class="field" style="left:323px;width:269px"><label>Member Name</label><div class="select">Name <svg width="14" height="8" viewBox="0 0 14 8"><path d="M1 1l6 6 6-6" stroke="#555" fill="none" stroke-width="1.5"/></svg></div></div>
  <div class="field" style="left:608px;width:183px"><label>Company</label><div class="select">Company <svg width="14" height="8" viewBox="0 0 14 8"><path d="M1 1l6 6 6-6" stroke="#555" fill="none" stroke-width="1.5"/></svg></div></div>
</div>
<a class="abs btn-explore" href="#">Explore Now <svg width="9" height="13" viewBox="0 0 9 13"><path d="M0 0l9 6.5L0 13z" fill="#fff"/></svg></a>

<!-- Welcome -->
<h2 class="abs welcome-title">Brindlewood Chamber Welcomes<br>New Members</h2>
<div class="abs body-copy welcome-copy">
  <p>The Chamber provides support to Brindlewood Business through enabling networking and interaction within the community, including Government, Council, Schools and Community Groups.</p>
  <p>The Chamber provides opportunities for you to meet and promote your business to a broad range of Brindlewood businesses, community groups and government bodies.</p>
</div>
<a class="abs btn-navy btn-learn" href="#">Learn More <svg width="15" height="15" viewBox="0 0 16 16"><circle cx="8" cy="8" r="8" fill="#fff"/><path d="M6.5 4.5L10 8l-3.5 3.5" stroke="#132a52" stroke-width="2" fill="none"/></svg></a>
<div class="abs welcome-photo" role="img" aria-label="Business meeting in a bright office, split by a diagonal white line"></div>

<!-- Services band -->
<svg class="abs services-bg" viewBox="0 0 1200 720" preserveAspectRatio="none" role="img" aria-label="Dark blue technology backdrop">
  <defs><linearGradient id="svcGrad" x1="0" y1="0" x2="1" y2="1"><stop offset="0" stop-color="#122449"/><stop offset=".55" stop-color="#1c3160"/><stop offset="1" stop-color="#0f1d3a"/></linearGradient></defs>
  <polygon points="0,81 1200,6 1200,648 0,715" fill="url(#svcGrad)"/>
</svg>

<div class="abs card card-light" style="left:207px;top:1428px">
  <svg width="60" height="52" viewBox="0 0 60 52" fill="none" stroke="#222" stroke-width="2"><circle cx="30" cy="14" r="8"/><path d="M16 38c0-8 6-13 14-13s14 5 14 13"/><circle cx="14" cy="24" r="6"/><circle cx="46" cy="24" r="6"/><path d="M2 46c0-7 5-11 12-11M58 46c0-7-5-11-12-11"/><path d="M10 46h40"/></svg>
  <h3>Member Directory</h3>
  <p>Equipped with storage, sorting, packing, warehousing fruits, and banana ripening at a large scale.</p>
</div>
<div class="abs card card-dark" style="left:481px;top:1325px;height:230px">
  <svg width="52" height="52" viewBox="0 0 52 52" fill="none" stroke="#fff" stroke-width="2"><rect x="3" y="8" width="46" height="40" rx="3"/><path d="M3 18h46M15 3v10M37 3v10"/><path d="M12 26h6M23 26h6M34 26h6M12 34h6M23 34h6M34 34h6M12 41h6M23 41h6"/></svg>
  <h3>Upcoming Events</h3>
  <p>To facilitate the development of agricultural and food business by providing high quality produce for the consumers</p>
</div>
<div class="abs card card-light" style="left:758px;top:1428px">
  <svg width="76" height="52" viewBox="0 0 76 52" fill="none" stroke="#222" stroke-width="2"><path d="M2 10l12-4 10 22-12 5z"/><path d="M74 10l-12-4-10 22 12 5z"/><path d="M24 14l10-4h10l8 6-10 4-6-3-8 6"/><path d="M22 30l8 8 4-3 4 4 4-3 4 3 6-6-8-10"/></svg>
  <h3>Join the Chamber</h3>
  <p>Red Delicious<br>Golden Delicious, Gala,<br>Royal Gala, Hayward Kiwi<br>Sunblush Kiwi</p>
</div>
<div class="abs card card-dark" style="left:481px;top:1590px;height:222px;padding-top:22px">
  <svg width="50" height="50" viewBox="0 0 50 50" fill="none" stroke="#fff" stroke-width="2"><circle cx="25" cy="27" r="21"/><path d="M25 6v21h21"/><path d="M30 2v20h18A20 20 0 0030 2z"/></svg>
  <h3>Business 2 Business</h3>
  <p>To grow into a sustainable agriculture and food products provider by ensuring supply sufficiency, high quality farming</p>
</div>

<!-- Book -->
<h2 class="abs book-title">Business 2 Business<br>A book and now a weekly webinar!!</h2>
<div class="abs body-copy book-copy">
  <p>Business 2 Business is a collaboration written by business members of Brindlewood Chamber of Commerce.</p>
  <p style="margin-bottom:14px">Our aim is to bring Business 2 your Business.</p>
  <p style="margin-bottom:12px">Get your copy now for $45 delivered or Order it and pick it up at a Chamber Event for $35</p>
  <p>For Webinar information, become a member (currently free), subscribe to our newsletter (free) or check out our <u>Circlefeed page.</u></p>
</div>
<div class="abs book-art" role="img" aria-label="Hardcover book Business 2 Business, compiled by Marla Fenwick"></div>

<!-- Connect band -->
<svg class="abs connect-bg" viewBox="0 0 1200 620" preserveAspectRatio="none" role="img" aria-label="Close-up of blue social app tiles">
  <defs><linearGradient id="cnGrad" x1="0" y1="0" x2="1" y2="1"><stop offset="0" stop-color="#1f3a7a"/><stop offset=".5" stop-color="#2a4a96"/><stop offset="1" stop-color="#142a5a"/></linearGradient></defs>
  <polygon points="0,117 1200,10 1200,565 0,610" fill="url(#cnGrad)"/>
  <polygon points="0,110 1200,0 1200,10 0,122" fill="#132a52"/>
  <polygon points="0,117 1200,8 1200,12 0,122" fill="#f3b11c"/>
</svg>
<h2 class="abs connect-title">More Connected Than Ever</h2>
<p class="abs connect-sub">Join our Circlefeed Group for even more access to our events, information and advocacy.</p>
<a class="abs btn-connect" href="#"><span class="sq"></span>CONNECT WITH CIRCLEFEED</a>

<!-- Sponsors -->
<h2 class="abs sponsor-title">We are proud to be affiliated with<br>the following sponsors:</h2>
<div class="abs sponsors">
  <div class="sponsor">Kestrel 94.1</div>
  <div class="sponsor" style="font-size:16px">Brindlewood Growth</div>
  <div class="sponsor">investBrindle</div>
  <div class="sponsor">Norvane Home</div>
</div>

<!-- Footer -->
<svg class="abs footer-bg" viewBox="0 0 1200 445" preserveAspectRatio="none">
  <polygon points="0,100 1200,18 1200,445 0,445" fill="#0d1a33"/>
  <polygon points="0,88 1200,6 1200,16 0,98" fill="#132a52"/>
  <polygon points="0,93 1200,11 1200,15 0,97" fill="#f3b11c"/>
</svg>

<div class="abs fcol" style="left:107px;top:3556px;width:240px">
  <h4>Contact Us</h4>
  <div class="contact-row"><svg width="12" height="16" viewBox="0 0 12 16"><path d="M6 1a5 5 0 015 5c0 4-5 9-5 9S1 10 1 6a5 5 0 015-5z" stroke="#fff" fill="none"/><circle cx="6" cy="6" r="1.8" fill="#fff"/></svg><span>BRINDLEWOOD CHAMBER OF COMMERCE<br>PO Box 318<br>Hollowmere QLD 4190</span></div>
  <div class="contact-row"><svg width="14" height="14" viewBox="0 0 24 24"><path d="M6.6 10.8a15 15 0 006.6 6.6l2.2-2.2a1 1 0 011-.25 11.4 11.4 0 003.6.57 1 1 0 011 1V20a1 1 0 01-1 1A17 17 0 013 4a1 1 0 011-1h3.5a1 1 0 011 1c0 1.25.2 2.45.57 3.57a1 1 0 01-.25 1z" fill="#fff"/></svg><span>(07) 5550 2716</span></div>
  <div class="contact-row"><svg width="15" height="11" viewBox="0 0 15 11"><rect x=".5" y=".5" width="14" height="10" stroke="#fff" fill="none"/><path d="M.5.5l7 5 7-5" stroke="#fff" fill="none"/></svg><span>admin@brindlewoodchamber.com.au</span></div>
</div>
<div class="abs fcol" style="left:382px">
  <h4>MEMBERSHIP</h4>
  <ul><li>Benefits</li><li>Community</li><li>Membership Directory</li><li>Contact</li><li>Committee</li><li>Past Committee Members</li><li>Business Distinction Awards</li></ul>
</div>
<div class="abs fcol" style="left:615px">
  <h4>EVENTS</h4>
  <ul><li>Brindlewood Business Expo</li><li>Events Schedule</li><li>Recordings</li><li>Business Distinction Awards</li><li>Brindlewood Business Expo</li><li>Terms</li><li>Privacy</li></ul>
</div>
<div class="abs fcol" style="left:842px;width:256px">
  <h4 style="font-size:13px;margin-bottom:12px">Never Miss Out</h4>
  <p style="line-height:18px;font-size:12.5px">Subscribe to the Chamber Newsletter and get information on upcoming events and information relevant to your business.</p>
  <div class="subscribe"><div class="input">Email address</div><div class="go">Subscribe</div></div>
</div>

<div class="abs footer-line"></div>
<p class="abs copyright">Copyright 2020 &nbsp;brindlewoodchamber</p>
<div class="abs foot-social"><span></span><span></span><span></span></div>

</body>
</html>
```